Magazine Ad for The Valmont Partners | ||
The Valmont Partners | ||
Clear Plans, Careful Oversight | ||
This ad should have a landscape orientation for a 1/2 page magazine spread, but must be easy to convert to a portrait orientation. | ||
Financial Services | ||
Target audience: Credit Union executives | ||
Must have our name and logo, our tagline, plus the following text: SERP Retirement Health Care Benefits Pre-Funding Contact info: Marcia Tolland 503.418-2731 www.valmontpartners.example |

```html
<!DOCTYPE html>
<html lang="en">
<head>
<meta charset="UTF-8">
<title>The Valmont Partners – Magazine Ad</title>
<link rel="stylesheet" href="https://fonts.googleapis.com/css2?family=Montserrat:wght@300;400;700&display=swap">
<style>
  :root {
    --paper: #ffffff;
    --forest: #1d4a1c;
    --forest-deep: #143815;
    --leaf: #3f7a31;
    --ink-green: #2a5a26;
    --muted: #9fb89a;
    --photo-light: #e8dccb;
    --photo-mid: #a88f74;
    --photo-dark: #4a3c32;
  }
  html, body {
    margin: 0;
    padding: 0;
    width: 1200px;
    height: 840px;
    overflow: hidden;
    background: var(--paper);
    font-family: "Montserrat", Arial, sans-serif;
  }
  .ad {
    position: relative;
    width: 1200px;
    height: 840px;
    background: var(--paper);
  }
  .headline-panel {
    position: absolute;
    left: 14px; top: 14px;
    width: 516px; height: 500px;
    background: var(--forest);
  }
  .headline {
    position: absolute;
    left: 50px; top: 110px;
    margin: 0;
    color: var(--paper);
    font-size: 58px;
    line-height: 70px;
    letter-spacing: 1px;
    text-transform: uppercase;
  }
  .headline .strong { font-weight: 700; display: block; }
  .headline .light { font-weight: 300; display: block; }
  .photo {
    position: absolute;
    left: 544px; top: 14px;
    width: 642px; height: 776px;
    background: linear-gradient(115deg, var(--photo-dark) 0%, var(--photo-mid) 40%, var(--photo-light) 75%, #f3ece2 100%);
  }
  .identity {
    position: absolute;
    left: 14px; top: 514px;
    width: 516px; height: 202px;
    background: var(--paper);
  }
  .brand {
    position: absolute;
    left: 36px; top: 58px;
    width: 240px;
  }
  .brand-mark {
    width: 34px; height: 34px;
    border-radius: 50%;
    background: var(--ink-green);
    margin: 0 0 10px 0;
  }
  .brand-name {
    margin: 0;
    color: var(--ink-green);
    font-weight: 700;
    font-size: 17px;
    line-height: 22px;
    white-space: nowrap;
  }
  .brand-tagline {
    margin: 6px 0 0;
    color: var(--ink-green);
    font-size: 11px;
    font-weight: 400;
    white-space: nowrap;
  }
  .services {
    position: absolute;
    left: 290px; top: 74px;
    margin: 0; padding: 0 0 0 18px;
    list-style: none;
    border-left: 1px solid var(--muted);
    color: var(--ink-green);
    font-size: 15px;
    line-height: 22px;
  }
  .services .lead { font-weight: 700; }
  .contact {
    position: absolute;
    left: 14px; top: 716px;
    width: 516px; height: 110px;
    background: var(--forest);
    border-left: 14px solid var(--leaf);
    box-sizing: border-box;
    color: var(--paper);
    padding: 18px 0 0 40px;
  }
  .contact-label {
    margin: 0;
    font-size: 13px;
    letter-spacing: 2px;
    color: var(--muted);
  }
  .contact-line {
    margin: 4px 0 0;
    font-size: 19px;
    font-weight: 400;
    letter-spacing: 0.5px;
    white-space: nowrap;
  }
  .footer-band {
    position: absolute;
    left: 530px; top: 790px;
    width: 656px; height: 36px;
    background: var(--forest-deep);
  }
</style>
</head>
<body>
  <div class="ad">
    <section class="headline-panel">
      <h1 class="headline">
        <span class="strong">Let us</span>
        <span class="strong">help you</span>
        <span class="light">plan for</span>
        <span class="light">the future</span>
      </h1>
    </section>

    <div class="photo" role="img" aria-label="Photograph of a smiling advisor shaking hands with a client across an office desk"></div>

    <section class="identity">
      <div class="brand">
        <div class="brand-mark"></div>
        <p class="brand-name">The Valmont Partners</p>
        <p class="brand-tagline">Clear Plans, Careful Oversight</p>
      </div>
      <ul class="services">
        <li class="lead">SERP</li>
        <li>Retirement Health Care</li>
        <li>Benefits Pre-Funding</li>
      </ul>
    </section>

    <section class="contact">
      <p class="contact-label">Contact</p>
      <p class="contact-line">Marcia Tolland 503.418-2731</p>
      <p class="contact-line">www.valmontpartners.example</p>
    </section>

    <div class="footer-band"></div>
  </div>
</body>
</html>
```